Wendelmarsh general contractors post card for mailing

Ideas: bathrooms, basements, kitchens, drywall, painting, landscaping, plumbing, electric, appliance, flooring, trim, sheds, decks, fences, home building, commercial construction, property management, lawn care/maintenance Just to list a few!!!

If we can't do it... it can't be done right.

turning dreams and aspirations into affordable reality.

Did your last contractor fail to meet your expectations? Let us provide affordable corrections.

Your single point of success for all your repair, replace, renovation, and building needs.

Trust us with all your projects large and small.

Target Market(s)

Home owners commercial property owners

Industry/Entity Type

Construction Company

Requirements
Must have
• phone number in red
Nice to have
• I would like to see greyscale background of commercial and suburban housing as a faded canvas backdrop.

```html
<!DOCTYPE html>
<html lang="en">
<head>
<meta charset="utf-8">
<title>Wendelmarsh Postcard</title>
<link rel="stylesheet" href="https://fonts.googleapis.com/css2?family=Tinos:wght@400;700&family=Cinzel:wght@600&family=Roboto:wght@700&display=swap">
<style>
  :root {
    --bg: #2a2a2c;
    --card: #ffffff;
    --navy: #1d3566;
    --blue: #2a63b8;
    --blue-light: #5c8fd6;
    --red: #d4201f;
    --ink: #2b2b2b;
    --grey-panel: #e9e9eb;
    --pill: #c9c9cc;
    --line: #8a8a8a;
  }
  * { margin: 0; padding: 0; box-sizing: border-box; }
  html, body { width: 900px; height: 1200px; overflow: hidden; }
  body { background: var(--bg); position: relative; font-family: "Tinos", serif; }

  .card { position: absolute; left: 54px; width: 792px; background: var(--card); overflow: hidden; box-shadow: 0 6px 18px rgba(0,0,0,.5); }

  /* front */
  .card-front { top: 24px; height: 546px; }
  .city-photo { position: absolute; left: 0; top: 0; width: 792px; height: 410px;
    background: linear-gradient(180deg, #c9d6e3 0%, #e6ebf0 30%, #8e9aa6 55%, #6f7f6a 75%, #4d6a3e 100%); }
  .front-swoosh { position: absolute; left: 0; top: 340px; width: 792px; height: 206px; }
  .brand { position: absolute; left: 130px; top: 420px; width: 240px; text-align: center; }
  .brand-mark { width: 44px; height: 44px; background: var(--navy); margin: 0 auto 8px; }
  .brand-name { font-family: "Cinzel", serif; font-weight: 600; font-size: 34px; color: var(--navy); letter-spacing: 1px; }
  .brand-tag { font-family: "Tinos", serif; font-size: 11px; color: var(--navy); letter-spacing: 3px; margin-top: 2px; }
  .front-phone { position: absolute; left: 520px; top: 430px; width: 220px; text-align: center; }
  .phone-icon { width: 28px; height: 28px; display: block; margin: 0 auto 4px; }
  .phone-number { font-family: "Roboto", sans-serif; font-weight: 700; font-size: 26px; color: var(--red); }

  /* back */
  .card-back { top: 585px; height: 555px; background: linear-gradient(135deg, #f4f4f5 0%, var(--grey-panel) 60%, #dcdcdf 100%); }
  .message { position: absolute; left: 24px; top: 22px; width: 370px; color: var(--ink); font-size: 15px; line-height: 1.3; }
  .headline { font-weight: 700; font-size: 19px; color: var(--navy); margin-bottom: 4px; white-space: nowrap; }
  .message p { margin-bottom: 2px; }
  .trust { color: var(--blue); font-size: 17px; text-align: center; margin: 22px 0 10px; white-space: nowrap; }
  .pill { display: block; width: 160px; margin: 0 auto 10px; padding: 5px 0; border-radius: 18px; background: var(--pill); text-align: center; font-size: 17px; color: var(--ink); box-shadow: inset 0 -2px 3px rgba(0,0,0,.15); }
  .services { text-align: center; font-size: 14.5px; line-height: 1.3; }
  .back-phone { margin-top: 22px; text-align: center; }
  .back-phone .phone-number { font-size: 24px; }
  .divider { position: absolute; left: 410px; top: 40px; width: 1px; height: 470px; background: var(--line); }
  .stamp-box { position: absolute; left: 620px; top: 40px; width: 120px; height: 135px; border: 2px solid var(--line); }
  .address-line { position: absolute; left: 470px; width: 270px; height: 1px; background: var(--line); }
</style>
</head>
<body>

<section class="card card-front">
  <div class="city-photo" role="img" aria-label="Downtown skyline with tall office towers and a green park under a cloudy sky"></div>
  <svg class="front-swoosh" viewBox="0 0 792 206" preserveAspectRatio="none">
    <path d="M0 40 Q396 120 792 10 L792 206 L0 206 Z" fill="#ffffff"/>
    <path d="M0 40 Q396 120 792 10" fill="none" stroke="#2a63b8" stroke-width="12"/>
    <path d="M0 56 Q396 136 792 26" fill="none" stroke="#5c8fd6" stroke-width="4"/>
  </svg>
  <div class="brand">
    <div class="brand-mark"></div>
    <div class="brand-name">WENDELMARSH</div>
    <div class="brand-tag">GENERAL CONTRACTORS</div>
  </div>
  <div class="front-phone">
    <svg class="phone-icon" viewBox="0 0 24 24"><circle cx="12" cy="12" r="11" fill="none" stroke="#d4201f" stroke-width="1.5"/><path d="M8 6.5l2 2-1.2 1.6c.7 1.5 1.8 2.6 3.3 3.3l1.6-1.2 2 2-1.3 1.6c-3.6-.3-7.1-3.8-7.4-7.4z" fill="#d4201f"/></svg>
    <div class="phone-number">1-866-555-0147</div>
  </div>
</section>

<section class="card card-back">
  <div class="message">
    <p class="headline">If we can't do it... it can't be done right.</p>
    <p>Turning dreams and aspirations into affordable reality.</p>
    <p>Did your last contractor fail to meet your expectations? Let us provide affordable corrections. Your single point of success for all your repair, replace, renovation, and building needs.</p>
    <p class="trust">Trust us with all your projects large and small.</p>
    <span class="pill">Just to list a few</span>
    <p class="services">Bathrooms, basements, kitchens, drywall, painting, landscaping, plumbing, electric, appliance, flooring, trim, sheds, decks, fences, home building, commercial construction, property management, lawn care/maintenance</p>
    <div class="back-phone">
      <svg class="phone-icon" viewBox="0 0 24 24"><circle cx="12" cy="12" r="11" fill="none" stroke="#d4201f" stroke-width="1.5"/><path d="M8 6.5l2 2-1.2 1.6c.7 1.5 1.8 2.6 3.3 3.3l1.6-1.2 2 2-1.3 1.6c-3.6-.3-7.1-3.8-7.4-7.4z" fill="#d4201f"/></svg>
      <div class="phone-number">1-866-555-0147</div>
    </div>
  </div>
  <div class="divider"></div>
  <div class="stamp-box"></div>
  <div class="address-line" style="top:300px"></div>
  <div class="address-line" style="top:345px"></div>
  <div class="address-line" style="top:390px"></div>
  <div class="address-line" style="top:435px"></div>
</section>

</body>
</html>
```